Sonstige Web-Design für Private Cloud Lösungen
Zielgruppe
Wir sind anbieter für Private Cloud Lösungen und benötigen eine Zeitgemäße Website, die ohne viel schnick schnack klar ausdrückt was wir machen.
Dabei die nötige Seriösität ausdrückt, welche hochsensible Daten benötigen.
Unsere Zielgruppe sind Unternehmen bis 250 MA
Die Farbgebung sollte an die des Logos angepasst sein, welches hier ebenfalls mit Farbcode hochgeladen wird.
Der Focus liegt auf Managed private Cloud und dem klaren kommitment Ihre Daten sicher in Deutschland
von der Landingpage soll es zur maximal 5 Unterseiten gehen.
1. Managed Private Cloud
2. Service Provider (Hier sollen unsere Dienstleistungen gelistet und auf einzelnen Seiten erklärt werden)
3. Trainings
4. Kontakt
Aufgabenstellung
Es sollte modern sein. Beim Besuch der Website soll auf der ersten Seite klar werden, was den Besucher erwartet jedoch ohne viel Worte.

```html
<!DOCTYPE html>
<html lang="de">
<head>
<meta charset="utf-8">
<title>Kivora – Private-Cloud-Lösungen</title>
<link href="https://fonts.googleapis.com/css2?family=Roboto:wght@400;500;700&display=swap" rel="stylesheet">
<style>
:root{
  --ink:#111;
  --dark:#2f2f2f;
  --card:#232323;
  --blue:#1a8fcf;
  --white:#fff;
  --muted:#d8d8d8;
  --text:#222;
}
*{box-sizing:border-box;margin:0;padding:0}
html,body{width:1200px;height:3097px;overflow:hidden}
body{font-family:'Roboto',sans-serif;color:var(--white);background:var(--dark);position:relative}
.abs{position:absolute}

/* Hero */
.hero{position:absolute;left:0;top:0;width:1200px;height:673px;background:var(--ink)}
.hero-photo{position:absolute;inset:0;background:
  radial-gradient(ellipse 380px 330px at 400px 250px,#4a3428 0%,#2a1d18 45%,transparent 80%),
  radial-gradient(ellipse 300px 420px at 880px 380px,#3a3f48 0%,#1c1f24 55%,transparent 85%),
  linear-gradient(90deg,#161210 0%,#100c0a 50%,#0a0a0b 100%)}
.brand{position:absolute;left:96px;top:34px;height:65px;display:flex;align-items:center;gap:10px}
.brand-mark{width:14px;height:14px;background:var(--blue)}
.brand-name{font-size:32px;font-weight:700;color:var(--white);letter-spacing:.5px}
.nav{position:absolute;top:62px;left:0;width:1200px;font-size:16.5px;font-weight:500}
.nav a{position:absolute;color:var(--white);text-decoration:none}
.hero-copy{position:absolute;left:537px;top:326px;width:560px}
.hero-copy h1{font-size:48px;font-weight:700;line-height:58px}
.hero-copy p{font-size:16.5px;line-height:26px;font-weight:500;margin-top:2px}

/* Partners */
.partners{position:absolute;left:0;top:673px;width:1200px;height:169px;background:var(--white)}
.partner{position:absolute;top:0;height:169px;display:flex;align-items:center;gap:10px;font-size:27px;font-weight:500;color:#333}
.partner-dot{width:18px;height:18px;border-radius:50%;background:var(--blue)}

/* Potential */
.intro{position:absolute;left:0;top:925px;width:1200px;text-align:center}
.intro h2{font-size:36px;font-weight:700;line-height:48px}
.intro p{font-size:16.5px;line-height:26.5px;font-weight:500;margin-top:10px}
.card{position:absolute;top:1075px;width:295px;height:320px;background:var(--card);box-shadow:0 0 28px rgba(0,0,0,.55);text-align:center;padding:0 18px}
.card svg{display:block;margin:30px auto 0;width:80px;height:80px}
.card h3{color:var(--blue);font-size:28px;font-weight:700;margin-top:20px;line-height:34px}
.card p{font-size:16.5px;line-height:26.5px;font-weight:500;margin-top:9px}

/* Features */
.feature-text{position:absolute;width:420px}
.feature-text .eyebrow{font-size:16.5px;font-weight:500;line-height:22px}
.feature-text h2{font-size:33px;font-weight:700;line-height:37.5px;margin-top:8px}
.feature-text p{font-size:16.5px;line-height:26.5px;font-weight:500;margin-top:14px}
.photo{position:absolute}
.photo-flag{background:linear-gradient(160deg,#9fbbe0 0%,#d8e2ee 40%,#8c857a 75%,#4a4540 100%)}
.photo-dc{background:linear-gradient(180deg,#6d7c8e 0%,#2b3038 45%,#c9d3de 75%,#eef2f7 100%)}
.photo-rack{background:linear-gradient(180deg,#3d3a36 0%,#8d9196 35%,#6f7479 65%,#2a2826 100%)}

/* CTA */
.cta{position:absolute;left:0;top:2779px;width:1200px;height:318px;background:var(--white);text-align:center;color:var(--text)}
.cta h2{color:var(--blue);font-size:52px;font-weight:700;margin-top:64px;line-height:60px}
.cta p{font-size:16.5px;line-height:26.5px;font-weight:500;margin-top:12px}
.cta-button{position:absolute;left:396px;top:204px;width:408px;height:59px;background:var(--blue);border-radius:6px;color:var(--white);font-size:22px;font-weight:700;line-height:59px;text-decoration:none}
</style>
</head>
<body>

<header class="hero">
  <div class="hero-photo" role="img" aria-label="Techniker verkabelt Server im dunklen Rechenzentrum"></div>
  <div class="brand"><span class="brand-mark"></span><span class="brand-name">Kivora</span></div>
  <nav class="nav">
    <a style="left:477px">Managed-Services</a>
    <a style="left:684px">Rechenzentrum</a>
    <a style="left:864px">Server-Housing</a>
    <a style="left:1044px">Kontakt</a>
  </nav>
  <div class="hero-copy">
    <h1>Private-Cloud-Lösungen</h1>
    <p>Lorem ipsum dolor sit amet, consectetuer adipiscing elit Aenean com modo ligula eget dolor. Aenean massa. Cum sociis natoque penatibus et magen piscing elit ligula eget dolor.</p>
  </div>
</header>

<section class="partners">
  <div class="partner" style="left:135px">Sentrafort</div>
  <div class="partner" style="left:360px"><span class="partner-dot"></span>Wolkenhaus</div>
  <div class="partner" style="left:570px">Teamwerk</div>
  <div class="partner" style="left:880px">Postarchiv</div>
</section>

<section class="intro">
  <h2>Schöpfen Sie Ihr volles Potenzial aus.</h2>
  <p>Lorem ipsum dolor sit amet, consectetuer adipiscing elit Aenean com modo ligula eget<br>dolor. Aenean massa. Cum sociis natoque penatibus escing elit ligula eget dolor.</p>
</section>

<div class="card" style="left:111px">
  <svg viewBox="0 0 80 80" fill="none" stroke="#1a8fcf" stroke-width="4">
    <path d="M4 6v70h72"/>
    <rect x="12" y="50" width="8" height="24" fill="#1a8fcf"/>
    <rect x="26" y="40" width="8" height="34" fill="#1a8fcf"/>
    <rect x="40" y="56" width="8" height="18" fill="#1a8fcf"/>
    <rect x="54" y="62" width="8" height="12" fill="#1a8fcf"/>
    <path d="M8 30l14-12 12 12 10-8"/>
    <circle cx="54" cy="24" r="12"/>
    <path d="M63 33l10 10"/>
  </svg>
  <h3>Kosten senken</h3>
  <p>Aenean com modo ligula eget dolor. Aenean massa. Cum sociis natoque pena tibus escing elit ligula eget dolor.</p>
</div>

<div class="card" style="left:452px">
  <svg viewBox="0 0 80 80" fill="#1a8fcf" stroke="#1a8fcf" stroke-width="4">
    <path d="M24 4v38M40 4v38M56 4v38" fill="none"/>
    <rect x="18" y="14" width="12" height="8" rx="2"/>
    <rect x="34" y="26" width="12" height="8" rx="2"/>
    <rect x="50" y="10" width="12" height="8" rx="2"/>
    <rect x="2" y="52" width="12" height="24" stroke="none"/>
    <path d="M16 56h26c6 0 6 8 0 8H30 M16 74h30l28-18c-2-6-8-6-12-3l-14 8" stroke="none"/>
    <path d="M16 54h24c8 0 8 10 0 10h8l16-10c6-4 12 2 8 6L50 76H16z" stroke="none"/>
  </svg>
  <h3>Mehr Kontrolle</h3>
  <p>Lorem ipsum dolor sit amet, conse ctetuer adipiscing elit Aenean com modo ligula eget dolor. Aenean massa.</p>
</div>

<div class="card" style="left:794px">
  <svg viewBox="0 0 80 80" fill="none" stroke="#1a8fcf" stroke-width="3.5">
    <ellipse cx="40" cy="8" rx="9" ry="4"/><path d="M31 8v12c0 5 18 5 18 0V8M31 14c0 5 18 5 18 0"/>
    <ellipse cx="10" cy="32" rx="9" ry="4"/><path d="M1 32v10c0 5 18 5 18 0V32"/>
    <ellipse cx="70" cy="32" rx="9" ry="4"/><path d="M61 32v10c0 5 18 5 18 0V32"/>
    <ellipse cx="40" cy="60" rx="9" ry="4"/><path d="M31 60v12c0 5 18 5 18 0V60M31 66c0 5 18 5 18 0"/>
    <path d="M40 26v28M22 38h12M46 38h12M40 40l-8-6M40 40l8-6"/>
  </svg>
  <h3>Leichter Skalieren</h3>
  <p>Lorem ipsum dolor sit amet, conse ctetuer adipiscing elit Aenean com modo ligula eget dolor. Aenean massa.</p>
</div>

<article>
  <div class="feature-text" style="left:137px;top:1588px">
    <div class="eyebrow">Managed Services</div>
    <h2>Ihre Daten in Deutschland</h2>
    <p>Lorem ipsum dolor sit amet, consectetuer adipiscing elit Aenean com modo ligula eget dolor. Aenean massa. Cum sociis natoque penatibus escing elit ligula eget dolor.</p>
  </div>
  <div class="photo photo-flag" style="left:599px;top:1550px;width:417px;height:270px" role="img" aria-label="Deutsche Flagge vor einem historischen Regierungsgebäude"></div>
</article>

<article>
  <div class="photo photo-dc" style="left:95px;top:1968px;width:418px;height:271px" role="img" aria-label="Heller Serverraum in einem Rechenzentrum"></div>
  <div class="feature-text" style="left:599px;top:1998px;width:440px">
    <div class="eyebrow">Rechenzentrum</div>
    <h2>Unsere Datencenter Zertifiziert nach ISO 27001</h2>
    <p>Lorem ipsum dolor sit amet, consectetuer adipiscing elit Aenean com modo ligula eget dolor. Aenean massa. Cum sociis natoque penatibus escing elit ligula eget dolor.</p>
  </div>
</article>

<article>
  <div class="feature-text" style="left:137px;top:2384px;width:430px">
    <div class="eyebrow">Server-Housing</div>
    <h2>Profitieren Sie von unserer Infrastruktur und bringen Sie Ihre Hardware zu uns</h2>
    <p>Lorem ipsum dolor sit amet, consectetuer adipiscing elit Aenean com modo ligula eget dolor. Aenean massa. Cum sociis natoque penatibus escing elit ligula eget dolor.</p>
  </div>
  <div class="photo photo-rack" style="left:599px;top:2391px;width:419px;height:271px" role="img" aria-label="Netzwerk-Switch-Chassis mit Modulen"></div>
</article>

<section class="cta">
  <h2>Sie möchten mehr erfahren?</h2>
  <p>Lorem ipsum dolor sit amet, consectetuer adipiscing elit Aenean com modo ligula eget<br>dolor. Aenean massa. Cum sociis natoque penatibus escing elit ligula eget dolor.</p>
  <a class="cta-button">Mit einem Experten sprechen</a>
</section>

</body>
</html>
```